Personal Trainer and Corporate Health Business

I need a business card for a new company I'm starting in Australia called "Brisk Vitality Partners" I will be providing a Personal training service as well as corporate health in companies.
The service provided is to help promote an active and healthy lifstyle.
The design should communicate a healthy lifestyle and also the benefits that this can have on a personal level and in the corporate environment and the benefits that flow from that.

Target Market(s)

Members of the public and Corporate

Industry/Entity Type

Environment

Requirements
Must have
• Company logo attached
Look and feel fresh and modern

Tag line: "Helping everyone move toward better health"

Lewis Norgate
Managing Director

m: 0417 596 304
e: lewis@briskvitalitypartners.com.au

www.briskvitalitypartners.com.au
Nice to have
• Can be 1 or 2 sided

```html
<!DOCTYPE html>
<html lang="en">
<head>
<meta charset="utf-8">
<title>Brisk Vitality Partners – Business Card</title>
<link href="https://fonts.googleapis.com/css2?family=Arimo:wght@400;700&family=Indie+Flower&display=swap" rel="stylesheet">
<style>
  :root {
    --bg: #d9d9d7;
    --card-white: #ffffff;
    --card-dark: #2e2e2f;
    --card-dark-edge: #232324;
    --brand-blue: #1f66b8;
    --brand-green: #9acd32;
    --text-light: #f2f2f2;
    --text-blue: #2f7ad0;
  }
  * { margin: 0; padding: 0; box-sizing: border-box; }
  html, body {
    width: 1200px; height: 900px; overflow: hidden;
    background: var(--bg);
    font-family: "Arimo", Arial, sans-serif;
  }
  .canvas { position: relative; width: 1200px; height: 900px; }

  .card {
    position: absolute;
    width: 640px; height: 370px;
    border-radius: 26px;
    overflow: hidden;
    box-shadow: 0 6px 18px rgba(0,0,0,.25);
    background: radial-gradient(ellipse at 50% 40%, var(--card-dark) 0%, var(--card-dark-edge) 100%);
  }
  .card--front { left: 130px; top: 40px; }
  .card--back  { left: 430px; top: 490px; }

  .brand {
    display: flex; align-items: center; gap: 12px;
    font-weight: 700; color: var(--brand-blue);
    font-size: 30px; letter-spacing: .5px;
    white-space: nowrap;
  }
  .brand__dot {
    width: 22px; height: 22px; border-radius: 50%;
    background: var(--brand-green); flex: none;
  }

  .front__top {
    position: absolute; left: 0; top: 0; width: 100%; height: 190px;
    background: var(--card-white);
    display: flex; align-items: center; justify-content: center;
  }
  .stripe { position: absolute; left: 0; width: 100%; }
  .stripe--green { background: var(--brand-green); }
  .stripe--blue  { background: var(--brand-blue); }
  .front .stripe--green { top: 190px; height: 8px; }
  .front .stripe--blue  { top: 198px; height: 8px; }

  .identity {
    position: absolute; left: 60px; top: 222px;
    display: flex; align-items: baseline; gap: 10px;
    white-space: nowrap;
  }
  .identity__name { color: var(--brand-green); font-size: 27px; letter-spacing: 1px; }
  .identity__bar  { color: var(--text-light); font-size: 24px; }
  .identity__role { color: var(--text-blue); font-size: 17px; letter-spacing: 1px; }

  .contacts { position: absolute; left: 118px; top: 266px; list-style: none; }
  .contacts li {
    display: flex; align-items: center; gap: 10px;
    color: var(--text-light); font-size: 18px; letter-spacing: .6px;
    height: 28px; white-space: nowrap;
  }
  .contacts svg { width: 18px; height: 18px; flex: none; }

  .back__logo {
    position: absolute; left: 0; top: 0; width: 100%; height: 250px;
    display: flex; align-items: center; justify-content: center;
  }
  .back .brand { font-size: 34px; }
  .back .stripe--green { top: 282px; height: 10px; }
  .back .stripe--blue  {
    top: 292px; height: 78px;
    display: flex; align-items: center; justify-content: center;
  }
  .tagline {
    font-family: "Indie Flower", cursive;
    color: #ffffff; font-size: 28px; letter-spacing: 2px;
    white-space: nowrap;
  }
</style>
</head>
<body>
<main class="canvas">

  <section class="card card--front front" aria-label="Business card front">
    <div class="front__top">
      <div class="brand"><span class="brand__dot"></span>Brisk Vitality Partners</div>
    </div>
    <div class="stripe stripe--green"></div>
    <div class="stripe stripe--blue"></div>

    <div class="identity">
      <span class="identity__name">Lewis Norgate</span>
      <span class="identity__bar">|</span>
      <span class="identity__role">Managing Director</span>
    </div>

    <ul class="contacts">
      <li>
        <svg viewBox="0 0 18 18" aria-hidden="true">
          <rect width="18" height="18" rx="3" fill="var(--brand-blue)"/>
          <path d="M5 3.5l2 .3.8 3-1.3 1a7 7 0 0 0 3.7 3.7l1-1.3 3 .8.3 2c-.1 1-1 1.5-2 1.4A10 10 0 0 1 3.6 5.5C3.5 4.5 4 3.6 5 3.5z" fill="#fff"/>
        </svg>
        0417 596 304
      </li>
      <li>
        <svg viewBox="0 0 18 18" aria-hidden="true">
          <rect x="0" y="3" width="18" height="12" rx="1" fill="var(--brand-blue)"/>
          <path d="M1 4l8 6 8-6" fill="none" stroke="#fff" stroke-width="1.4"/>
        </svg>
        lewis@briskvitalitypartners.com.au
      </li>
      <li>
        <svg viewBox="0 0 18 18" aria-hidden="true">
          <g fill="none" stroke="var(--brand-blue)" stroke-width="1.5">
            <circle cx="9" cy="9" r="7.5"/>
            <ellipse cx="9" cy="9" rx="3.3" ry="7.5"/>
            <path d="M1.5 9h15M3 5h12M3 13h12"/>
          </g>
        </svg>
        www.briskvitalitypartners.com.au
      </li>
    </ul>
  </section>

  <section class="card card--back back" aria-label="Business card back">
    <div class="back__logo">
      <div class="brand"><span class="brand__dot"></span>Brisk Vitality Partners</div>
    </div>
    <div class="stripe stripe--green"></div>
    <div class="stripe stripe--blue">
      <p class="tagline">"Helping everyone move toward better health"</p>
    </div>
  </section>

</main>
</body>
</html>
```